Funeral Services Site

We need a website for a Funeral Services company. The old website is: www.rouwcentrumkorvelaer.be We need the same structure and text.

Target Market(s)

Customers.

Coding

Coded - Design and coding required

Number of Pages Required

4 page

Font styles to use
Serif
Sans Serif
Script

```html
<!DOCTYPE html>
<html lang="en">
<head>
<meta charset="utf-8">
<title>Funeral home Korvelaer</title>
<link href="https://fonts.googleapis.com/css2?family=Roboto:wght@300;400;500;700;900&family=Merriweather:wght@400;700&display=swap" rel="stylesheet">
<style>
:root{
  --purple:#7b3ff2;
  --purple-dark:#6a2fe0;
  --ink:#222;
  --text:#555;
  --dark:#2b2b2b;
  --darker:#1d1d1d;
  --white:#fff;
  --light:#f4f4f4;
}
*{box-sizing:border-box;margin:0;padding:0}
html,body{width:764px;height:1200px;overflow:hidden}
body{font-family:"Roboto",sans-serif;color:var(--text);background:var(--white);position:relative}
.topbar{height:28px;background:var(--dark);color:#ccc;font-size:8px;display:flex;align-items:center;justify-content:space-between;padding:0 40px}
.topbar .info{display:flex;gap:16px}
.topbar span{display:flex;align-items:center;gap:4px}
.topbar svg{width:8px;height:8px;fill:#ccc}
.navbar{height:70px;display:flex;align-items:center;justify-content:space-between;padding:0 40px;background:var(--white)}
.brand{font-family:"Merriweather",serif;font-weight:700;font-size:17px;color:var(--ink);line-height:1.05;display:flex;align-items:center;gap:8px}
.brand .mark{width:14px;height:14px;background:var(--purple);border-radius:50%}
.brand small{font-size:17px}
.menu{display:flex;gap:24px;font-size:10px;color:var(--ink);list-style:none}
.hero{height:227px;position:relative;text-align:center;color:var(--white);display:flex;flex-direction:column;align-items:center;justify-content:center}
.hero-bg{position:absolute;inset:0;background:linear-gradient(180deg,#5a5a5a 0%,#3a3a3a 55%,#2a2a2a 100%)}
.hero-content{position:relative}
.hero .eyebrow{font-size:10px;letter-spacing:1px;text-transform:uppercase;font-weight:500}
.hero h1{font-size:22px;font-weight:900;letter-spacing:.5px;margin:6px 0 18px}
.buttons{display:flex;gap:12px;justify-content:center}
.btn{display:inline-block;width:72px;height:24px;line-height:22px;font-size:9px;border:1px solid var(--white);color:var(--white);text-align:center}
.btn-primary{background:var(--purple);border-color:var(--purple)}
.about{height:180px;text-align:center;padding:42px 95px 0}
.section-title{font-size:16px;font-weight:900;color:var(--ink);text-transform:uppercase;letter-spacing:.5px}
.about p{font-size:8px;line-height:1.55;margin-top:14px}
.band{height:56px;background:var(--purple);display:flex;align-items:center;justify-content:center;font-family:"Merriweather",serif;color:var(--white);font-size:15px}
.organization{height:292px;display:flex;gap:30px;padding:36px 40px 0 80px}
.org-photos{position:relative;width:300px;height:220px}
.photo{position:absolute}
.photo-a{left:0;top:0;width:120px;height:150px;background:linear-gradient(160deg,#c7b9a5,#7d6b5a)}
.photo-b{left:110px;top:40px;width:140px;height:175px;background:linear-gradient(160deg,#eeeeee,#b8c3b0)}
.org-text{flex:1;padding-top:22px}
.org-text h2{font-size:14px;font-weight:900;color:var(--ink);line-height:1.3}
.org-text p{font-size:7.5px;line-height:1.55;margin:12px 0 10px}
.ticks{list-style:none;font-size:7.5px;line-height:1.5}
.ticks li{display:flex;gap:6px;margin-bottom:4px}
.ticks svg{flex:none;width:8px;height:8px;margin-top:2px}
.cta{height:167px;position:relative;text-align:center;color:var(--white);display:flex;flex-direction:column;justify-content:center;align-items:center}
.cta-bg{position:absolute;inset:0;background:linear-gradient(180deg,#4d4b4c,#373536)}
.cta-content{position:relative}
.cta h2{font-size:15px;font-weight:900;line-height:1.3;text-transform:uppercase;margin-bottom:16px}
.footer{height:152px;background:var(--darker);color:#bbb;display:flex;gap:34px;padding:24px 40px 0}
.footer .col{font-size:7.5px;line-height:1.55}
.footer .about-col{width:170px}
.footer .brand{color:var(--white);font-size:15px;margin-bottom:8px}
.footer .brand small{font-size:15px}
.footer h3{font-size:11px;color:var(--white);font-weight:700;margin-bottom:12px}
.contact-col{width:180px}
.contact-col li{list-style:none;display:flex;gap:6px;align-items:center;margin-bottom:10px}
.contact-col svg{width:9px;height:9px;fill:#bbb}
.condole-col{flex:1}
.field{height:52px;background:#2e2e2e;border:1px solid #3a3a3a;color:#777;padding:5px 7px;font-size:7px}
.send{margin-top:8px;width:70px;height:18px;background:var(--purple);color:var(--white);font-size:8px;text-align:center;line-height:18px;margin-left:auto}
.bottombar{height:25px;background:#141414;color:#888;font-size:7px;display:flex;align-items:center;justify-content:space-between;padding:0 40px}
.social{display:flex;gap:6px}
.social span{width:9px;height:9px;border-radius:50%;background:#888}
</style>
</head>
<body>
<header>
  <div class="topbar">
    <div class="info">
      <span><svg viewBox="0 0 10 10"><path d="M5 0a3.5 3.5 0 0 0-3.5 3.5C1.5 6 5 10 5 10s3.5-4 3.5-6.5A3.5 3.5 0 0 0 5 0zm0 5a1.5 1.5 0 1 1 0-3 1.5 1.5 0 0 1 0 3z"/></svg>2890 Sint-Amant</span>
      <span><svg viewBox="0 0 10 10"><path d="M0 2h10v6H0z M0 2l5 3.5L10 2" /></svg>info@rouwcentrumkorvelaer.be</span>
      <span><svg viewBox="0 0 10 10"><path d="M2 0l2 2.5-1 1.2a6 6 0 0 0 3.3 3.3l1.2-1L10 8 8.5 10C4 10 0 6 0 1.5z"/></svg>012 34 56 78</span>
    </div>
    <div>Language : Dutch</div>
  </div>
  <nav class="navbar">
    <div class="brand"><span class="mark"></span><span>Funeral home<br><small>Korvelaer</small></span></div>
    <ul class="menu">
      <li>Home</li><li>About Us</li><li>Condole Online</li><li>Order Flowers</li><li>Contact</li>
    </ul>
  </nav>
</header>

<section class="hero">
  <div class="hero-bg" role="img" aria-label="Dark photograph of a farewell ceremony with flowers"></div>
  <div class="hero-content">
    <div class="eyebrow">Funeral home Korvelaer bvba</div>
    <h1>A PERSONAL SERVICE IN FAREWELL GUIDANCE</h1>
    <div class="buttons"><span class="btn btn-primary">Contact Us</span><span class="btn">Call Now</span></div>
  </div>
</section>

<section class="about">
  <h2 class="section-title">About Us</h2>
  <p>Saying goodbye to a loved one is one of the toughest things in a lifetime. Funeral home Korvelaer in Sint-Amant takes care of all the practical and administrative matters involved. So you can say goodbye in peace. Our people have a very long experience in farewell guidance and stand by you 24 hours a day, 7 days a week. Our fully renovated funeral home is open to you and your acquaintances, so that you can gather your loved ones at any time of the day.</p>
</section>

<div class="band">Mourning center Korvelaer, a complete service in mourning and farewell guidance</div>

<section class="organization">
  <div class="org-photos">
    <div class="photo photo-a" role="img" aria-label="Photograph of a chapel interior with candles"></div>
    <div class="photo photo-b" role="img" aria-label="Photograph of white funeral flowers on a coffin"></div>
  </div>
  <div class="org-text">
    <h2>ORGANIZATION FUNERAL &amp;<br>WORSHIP</h2>
    <p>The organization of the funeral ceremony is a moment of reflection, where the personality of the deceased can be beautifully highlighted. Our team will assist you in this and select the most beautiful texts, songs and photos with you in order to arrive at an appropriate and worthy goodbye. The funeral can take place in your parish church or in our auditorium if you wish, which can accommodate a maximum of 150 guests. We can arrange the following for you:</p>
    <ul class="ticks">
      <li><svg viewBox="0 0 10 10"><circle cx="5" cy="5" r="5" fill="#7b3ff2"/><path d="M2.8 5.2l1.5 1.5 3-3.2" stroke="#fff" stroke-width="1.2" fill="none"/></svg>A quiet vigil the evening before the funeral</li>
      <li><svg viewBox="0 0 10 10"><circle cx="5" cy="5" r="5" fill="#7b3ff2"/><path d="M2.8 5.2l1.5 1.5 3-3.2" stroke="#fff" stroke-width="1.2" fill="none"/></svg>Prayer service with photo projection</li>
      <li><svg viewBox="0 0 10 10"><circle cx="5" cy="5" r="5" fill="#7b3ff2"/><path d="M2.8 5.2l1.5 1.5 3-3.2" stroke="#fff" stroke-width="1.2" fill="none"/></svg>Eucharistic celebration with a priest on Tuesday and Friday in the parish of Sint-Amant</li>
    </ul>
  </div>
</section>

<section class="cta">
  <div class="cta-bg" role="img" aria-label="Dark photograph of flower arrangements"></div>
  <div class="cta-content">
    <h2>Do you have any questions or would you like to call in<br>our funeral home? Contact us. We are here for you</h2>
    <div class="buttons"><span class="btn btn-primary">Contact Us</span><span class="btn">Call Now</span></div>
  </div>
</section>

<footer>
  <div class="footer">
    <div class="col about-col">
      <div class="brand"><span>Funeral home<br><small>Korvelaer</small></span></div>
      <p>Saying goodbye to a loved one is one of the toughest things in a lifetime. Funeral home Korvelaer in Sint-Amant takes care of all the practical and administrative matters involved. So you can say goodbye in peace.</p>
    </div>
    <div class="col contact-col">
      <h3>CONTACT US</h3>
      <ul>
        <li><svg viewBox="0 0 10 10"><path d="M5 0a3.5 3.5 0 0 0-3.5 3.5C1.5 6 5 10 5 10s3.5-4 3.5-6.5A3.5 3.5 0 0 0 5 0zm0 5a1.5 1.5 0 1 1 0-3 1.5 1.5 0 0 1 0 3z"/></svg>Kerkstraat 12, 2890 Sint-Amant</li>
        <li><svg viewBox="0 0 10 10"><path d="M2 0l2 2.5-1 1.2a6 6 0 0 0 3.3 3.3l1.2-1L10 8 8.5 10C4 10 0 6 0 1.5z"/></svg>012 34 56 78</li>
        <li><svg viewBox="0 0 10 10"><path d="M0 2h10v6H0z"/></svg>www.rouwcentrumkorvelaer.be</li>
      </ul>
    </div>
    <div class="col condole-col">
      <h3>CONDOLE ONLINE</h3>
      <div class="field">Write your message</div>
      <div class="send">Send</div>
    </div>
  </div>
  <div class="bottombar">
    <span>© 2018 Funeral home Korvelaer · Sitemap · Privacy Policy</span>
    <div class="social"><span></span><span></span><span></span></div>
  </div>
</footer>
</body>
</html>
```